Brackwell Renovations needs a website.

I need a platform for clients to go and learn about what my company does, see pictures of projects, and contact me about their projects. I am a residential remodeler specializing in general contracting services for kitchens, bathrooms, basements, additions, custom interiors, and more. I have attached my logo to be incorporated.

```html
<!DOCTYPE html>
<html lang="en">
<head>
<meta charset="utf-8">
<title>Brackwell Renovations – Website Design Presentation</title>
<link rel="stylesheet" href="https://fonts.googleapis.com/css2?family=Cinzel:wght@400;600&family=Roboto:wght@300;400;500;700&display=swap">
<style>
:root{
  --board:#0e4f47;
  --teal:#1bbfb3;
  --teal-soft:#d3f4f0;
  --white:#ffffff;
  --ink:#1d1d1d;
  --muted:#6b6b6b;
  --night:#000000;
  --dusk:#2a2723;
  --grey:#f3f3f3;
  --amber:#f5b400;
  --photo-warm:linear-gradient(135deg,#c9b79c,#8a6f52 60%,#4d3f33);
  --photo-light:linear-gradient(135deg,#eceae4,#cfc6b6 60%,#a99a85);
  --photo-dark:linear-gradient(135deg,#3b342c,#1f1b17 60%,#5b4632);
  --photo-site:linear-gradient(135deg,#9fb4c8,#d7c6a6 55%,#e0873a);
}
*{margin:0;padding:0;box-sizing:border-box}
html,body{width:1200px;height:2581px;overflow:hidden}
body{background:var(--board);font-family:"Roboto",sans-serif;font-weight:300;color:var(--white);position:relative}
.abs{position:absolute}

/* left presentation panel */
.intro{position:absolute;left:43px;top:92px;width:430px}
.label{font-weight:700;font-size:21px;letter-spacing:.2px}
.font-sample-display{font-family:"Cinzel",serif;font-size:46px;line-height:1;margin-top:14px}
.font-sample-body{font-size:36px;line-height:1.1;margin-top:2px}
.swatches{display:flex;gap:12px;margin-top:10px}
.swatch{width:124px;height:88px;border:2px solid #0a3d37;border-radius:8px}
.note{font-size:25px;line-height:1.22;margin-top:28px}
.view-title{position:absolute;top:38px;font-weight:700;font-size:22px;letter-spacing:.3px}

/* screens */
.screen{position:absolute;overflow:hidden;background:var(--white);color:var(--ink)}
.desktop{left:488px;top:83px;width:345px;height:2248px}
.mobile{left:923px;top:83px;width:213px;height:2407px}
.photo{position:absolute;background:var(--photo-warm)}
.photo.light{background:var(--photo-light)}
.photo.dark{background:var(--photo-dark)}
.photo.site{background:var(--photo-site)}
.topbar{position:absolute;left:0;top:0;width:100%;background:var(--night);color:#ddd;font-size:3px;display:flex;align-items:center;gap:10px;padding:0 10px}
.nav{position:absolute;left:0;width:100%;background:var(--white);display:flex;align-items:center;justify-content:space-between;padding:0 40px;font-size:3.4px;color:#333;font-weight:400}
.nav-links{display:flex;gap:8px}
.brand{display:flex;align-items:center;gap:2px;font-weight:700;color:#2b2b2b;letter-spacing:.2px;text-transform:uppercase}
.brand-mark{width:6px;height:6px;background:#2b2b2b}
.hero{position:absolute;left:0;width:100%;background:linear-gradient(180deg,#1d2430 0%,#3a2f26 55%,#201a15 100%);z-index:2;text-align:center;color:#fff}
.hero h1{font-family:"Cinzel",serif;font-weight:400;line-height:1.05}
.hero p{font-weight:400;line-height:1.35}
.fade{position:absolute;left:0;width:100%;background:linear-gradient(180deg,#fff 0%,var(--teal-soft) 35%,var(--teal) 100%)}
.wedge{position:absolute;left:0;width:100%;background:#fff}
.h-teal{color:var(--teal);font-weight:300;line-height:1.1}
.copy{color:var(--muted);line-height:1.45;font-weight:400}
.pill{position:absolute;border-radius:10px;text-align:center;font-weight:500}
.pill.solid{background:var(--teal);color:#fff}
.pill.soft{background:#c9f0e6;color:var(--teal)}
.about{position:absolute;left:0;width:100%;background:linear-gradient(180deg,#2f2b27,#17130f);color:#fff;text-align:center}
.stat b{display:block;color:var(--teal);font-weight:300}
.stat span{display:block;color:#ddd}
.services{position:absolute;left:0;width:100%;background:var(--grey);text-align:center}
.card{position:absolute;text-align:left}
.card h4{color:var(--teal);font-weight:500}
.card p{color:var(--muted);font-weight:400;line-height:1.35}
.card a{color:#333;font-weight:500;text-decoration:underline}
.projects{position:absolute;left:0;width:100%;background:var(--night);text-align:center}
.grid{position:absolute;display:grid;gap:2px}
.grid .tile{position:relative;background:var(--photo-light)}
.grid .tile:nth-child(3n+2){background:var(--photo-warm)}
.grid .tile:nth-child(4n){background:var(--photo-dark)}
.quote{color:#555;font-weight:400;line-height:1.4}
.avatar{display:inline-block;border-radius:50%;background:#d8b79c;vertical-align:middle}
.trusted{color:var(--teal);font-weight:500;line-height:1.25}
.contact{position:absolute;left:0;width:100%;background:var(--white)}
.field{position:absolute;border:.5px solid #cfcfcf;background:#fff;color:#aaa;font-weight:400;padding:1px 2px}
.submit{position:absolute;background:var(--amber);color:#fff;border-radius:10px;text-align:center;font-weight:500}
.footer-line{position:absolute;left:0;width:100%;border-top:.5px solid #ddd}
.legal{position:absolute;left:0;width:100%;background:#f5efe3;color:#666;font-weight:400}
</style>
</head>
<body>

<!-- presentation notes -->
<section class="intro">
  <div class="label">FONT&nbsp; USED:</div>
  <div class="font-sample-display">Cinzel</div>
  <div class="font-sample-body">Roboto Light</div>
  <div class="label" style="margin-top:66px">COLOR THEME:</div>
  <div class="swatches">
    <div class="swatch" style="background:var(--teal)"></div>
    <div class="swatch" style="background:var(--teal-soft)"></div>
    <div class="swatch" style="background:var(--white)"></div>
  </div>
  <p class="note" style="margin-top:52px">I am excited to submit my sample for your design project.</p>
  <p class="note">With my experience, I am fully equipped to assist, implement, and maintain the project for short or long-term contract, ensuring consistent quality and support.</p>
  <p class="note">I am readily available and flexible to work within your timezone, prioritizing clear communication and client satisfaction.</p>
  <p class="note">If you wish to revise this design, I’d be delighted to make any adjustments to meet your vision perfectly.</p>
  <p class="note">Sincerely,</p>
</section>

<h2 class="view-title" style="left:493px">DESKTOP VIEW</h2>
<h2 class="view-title" style="left:924px">TABLET / MOBILE VIEW</h2>

<!-- ================= DESKTOP ================= -->
<main class="screen desktop" aria-label="Desktop homepage">
  <div class="topbar" style="height:13px">
    <span>☎ 0400 123 456</span><span>✉ info@brackwell.com.au</span><span>⌖ PO Box 1180, Eastmere Q 4100</span>
  </div>
  <nav class="nav" style="top:13px;height:17px">
    <div class="brand" style="font-size:4px"><span class="brand-mark"></span>Brackwell Renovations</div>
    <div class="nav-links"><span>Home</span><span>Our Service</span><span>Product</span><span>Pricing</span><span>About Us</span><span>Contact Us</span></div>
  </nav>

  <header class="hero" role="img" aria-label="Photo of a spacious living room with city view at dusk" style="top:30px;height:165px;clip-path:polygon(0 0,100% 0,100% 88%,62% 100%,0 91%)">
    <h1 style="font-size:11px;margin-top:26px">Crafting Your Dream Home,<br>Room by Room</h1>
    <p style="font-size:3.6px;width:240px;margin:4px auto 0">At Brackwell Renovation, we transform houses into homes with expert residential remodeling services. Specializing in kitchens, bathrooms, basements, additions, and custom interiors, we bring craftsmanship and care to every project. Discover how we can elevate your living space today.</p>
  </header>

  <section class="fade" style="top:170px;height:257px">
    <p class="copy abs" style="left:42px;top:67px;width:190px;font-size:3.4px">At Brackwell Renovation, we transform houses into homes with expert residential remodeling services. Specializing in kitchens, bathrooms, basements, additions, and custom interiors, we bring craftsmanship and care to every project. Discover how we can elevate your living space today.</p>
    <div class="pill solid" style="left:266px;top:72px;width:36px;height:12px;font-size:4px;line-height:12px">CALL US</div>
    <div class="photo light" role="img" aria-label="Living room with sculptural lamp" style="left:42px;top:107px;width:83px;height:103px"></div>
    <div class="photo" role="img" aria-label="Bright room with plants and armchairs" style="left:131px;top:107px;width:83px;height:103px"></div>
    <div class="photo" role="img" aria-label="Lounge with timber ceiling" style="left:219px;top:107px;width:83px;height:103px"></div>
    <div class="wedge" style="top:222px;height:36px;clip-path:polygon(0 100%,66% 0,100% 60%,100% 100%)"></div>
  </section>

  <section aria-label="Who we are">
    <h2 class="h-teal abs" style="left:90px;top:443px;font-size:11px">Who We Are?</h2>
    <p class="copy abs" style="left:166px;top:442px;width:136px;font-size:3.3px">With years of experience in general contracting, Brackwell Renovation is your trusted partner for residential remodeling. We pride ourselves on delivering high-quality renovations tailored to your vision, whether it’s a modern kitchen, a spa-like bathroom, or a custom basement retreat. Our commitment to detail, reliability, and client satisfaction sets us apart. Let us bring your ideas to life with precision and style.</p>
    <div class="photo light" role="img" aria-label="White kitchen with island and stools" style="left:42px;top:491px;width:260px;height:117px"></div>

    <h3 class="h-teal abs" style="left:42px;top:671px;font-size:11px">Sleek Kitchen with<br>Clean Accents</h3>
    <p class="copy abs" style="left:42px;top:708px;width:95px;font-size:3.3px">Step into elegance with a kitchen that’s as functional as it is beautiful. At Brackwell Renovation, we blend expert craftsmanship with custom design to create spaces that inspire daily living. This remodel showcases our dedication to quality and style.</p>
    <div class="pill soft" style="left:42px;top:761px;width:30px;height:10px;font-size:5px;line-height:10px">Call Us</div>
    <div class="photo dark" role="img" aria-label="Double-height living room with stone feature wall" style="left:165px;top:630px;width:137px;height:182px"></div>
  </section>

  <section class="fade" style="top:812px;height:182px;background:linear-gradient(180deg,#fff 0%,var(--teal-soft) 40%,var(--teal) 100%)">
    <div class="photo" role="img" aria-label="Dining area with pendant lights and artwork" style="left:42px;top:13px;width:137px;height:153px"></div>
    <h3 class="h-teal abs" style="left:195px;top:43px;font-size:11px">Finished Basement<br>with Cozy Seating</h3>
    <p class="copy abs" style="left:195px;top:80px;width:100px;font-size:3.3px">Unlock the potential of your basement with Brackwell Renovation. This inviting lounge demonstrates our ability to turn unused spaces into warm, functional retreats—perfect for family time or quiet evenings.</p>
    <div class="pill soft" style="left:198px;top:125px;width:30px;height:10px;font-size:5px;line-height:10px;background:#e0f8f4">Call Us</div>
  </section>

  <section class="about" role="img" aria-label="Dim living room backdrop" style="top:994px;height:195px">
    <p style="font-size:9px;margin-top:39px;font-weight:400">About Us</p>
    <p style="font-size:12px;color:var(--teal);font-weight:300">Brackwell Renovation</p>
    <p style="font-size:3.3px;width:245px;margin:4px auto 0;font-weight:400;line-height:1.4">At Brackwell Renovation, we transform houses into homes with expert residential remodeling services. Specializing in kitchens, bathrooms, basements, additions, and custom interiors, we bring craftsmanship and care to every project. Discover how we can elevate your living space today.</p>
    <div class="pill solid" style="left:149px;top:99px;width:46px;height:11px;font-size:5px;line-height:11px;border-radius:1px">Contact Us</div>
    <div class="abs" style="left:50px;top:133px;width:250px;display:flex;justify-content:space-between">
      <div class="stat"><b style="font-size:20px">175</b><span style="font-size:4px">Happy clients</span></div>
      <div class="stat"><b style="font-size:20px">300+</b><span style="font-size:4px">Projects completed</span></div>
      <div class="stat"><b style="font-size:20px">9+</b><span style="font-size:4px">Projects Managed</span></div>
      <div class="stat"><b style="font-size:20px">180+</b><span style="font-size:4px">Dedicated employees</span></div>
    </div>
  </section>

  <section class="services" style="top:1189px;height:380px">
    <h2 class="h-teal" style="font-size:13px;margin-top:22px">Our Services</h2>
    <p class="copy" style="font-size:4.2px">We also offer custom interiors and more—contact us to discuss your unique project!</p>
    <article class="card" style="left:42px;top:87px;width:126px">
      <div class="photo site" role="img" aria-label="Builder on a residential site" style="position:relative;width:126px;height:72px"></div>
      <h4 style="font-size:4.5px;margin-top:14px">Kitchens</h4>
      <p style="font-size:3.4px;width:80px">From custom cabinetry to open-plan designs, we create kitchens that blend functionality with elegance</p>
      <a style="font-size:3.4px">Read More</a>
    </article>
    <article class="card" style="left:176px;top:87px;width:126px">
      <div class="photo site" role="img" aria-label="Contractors reviewing plans" style="position:relative;width:126px;height:72px"></div>
      <h4 style="font-size:4.5px;margin-top:14px">Bathrooms</h4>
      <p style="font-size:3.4px;width:85px">Turn your bathroom into a luxurious oasis with our expert tiling, fixtures, and layouts</p>
      <a style="font-size:3.4px">Read More</a>
    </article>
    <article class="card" style="left:42px;top:224px;width:126px">
      <div class="photo site" role="img" aria-label="Engineers with tablet on site" style="position:relative;width:126px;height:72px"></div>
      <h4 style="font-size:4.5px;margin-top:14px">Basements &amp; Additions</h4>
      <p style="font-size:3.4px;width:85px">Expand your living space with beautifully crafted basements and seamless home additions</p>
      <a style="font-size:3.4px">Read More</a>
    </article>
    <article class="card" style="left:176px;top:224px;width:126px">
      <div class="photo site" role="img" aria-label="Team studying drawings on site" style="position:relative;width:126px;height:72px"></div>
      <h4 style="font-size:4.5px;margin-top:14px">Rooms</h4>
      <p style="font-size:3.4px;width:85px">From custom cabinetry to open-plan designs, we create kitchens that blend functionality with elegance</p>
      <a style="font-size:3.4px">Read More</a>
    </article>
  </section>

  <section class="projects" style="top:1557px;height:440px">
    <svg class="abs" style="left:0;top:0" width="345" height="10" viewBox="0 0 345 10" aria-hidden="true"><path d="M0 0H345V4C300 8 260 1 210 5S110 2 60 6S20 3 0 5Z" fill="#f3f3f3"/></svg>
    <h2 class="h-teal" style="font-size:13px;margin-top:12px">Our Project</h2>
    <div class="grid" role="img" aria-label="Gallery of finished interior projects" style="left:42px;top:50px;width:260px;height:193px;grid-template-columns:repeat(4,1fr);grid-template-rows:repeat(3,1fr)">
      <div class="tile"></div><div class="tile"></div><div class="tile"></div><div class="tile"></div>
      <div class="tile"></div><div class="tile"></div><div class="tile"></div><div class="tile"></div>
      <div class="tile"></div><div class="tile"></div><div class="tile"></div><div class="tile"></div>
    </div>
    <p class="quote" style="font-size:4px;margin-top:283px">“What really turned me over was the ability to understand how everything works<br>without any prior knowledge”</p>
    <p style="font-size:3.5px;color:var(--amber);margin-top:3px"><span class="avatar" style="width:12px;height:12px"></span> John Doe</p>
    <p class="trusted" style="font-size:8.5px;margin-top:30px">Your Trusted Partner in Construction<br>Oversight and Planning</p>
    <p style="font-size:4.5px;color:#ccc">Harbourline Australia Pty Ltd</p>
  </section>

  <section class="contact" style="top:1965px;height:283px;clip-path:polygon(0 22px,50% 0,100% 22px,100% 100%,0 100%)">
    <div class="brand abs" style="left:130px;top:34px;font-size:6px"><span class="brand-mark" style="width:9px;height:9px"></span>Brackwell Renovations</div>
    <h2 class="h-teal abs" style="left:58px;top:93px;font-size:13px">Contact Us</h2>
    <p class="copy abs" style="left:58px;top:111px;font-size:4px;color:#444">We would love to speak with you.<br>Feel free to reach us</p>
    <h3 class="h-teal abs" style="left:58px;top:132px;font-size:8px">Address</h3>
    <p class="copy abs" style="left:58px;top:142px;font-size:3.5px">PO Box 1180, Eastmere Q 4100</p>
    <h3 class="h-teal abs" style="left:58px;top:158px;font-size:8px">Phone</h3>
    <p class="copy abs" style="left:58px;top:169px;font-size:3.5px">0400 123 456</p>
    <h3 class="h-teal abs" style="left:58px;top:185px;font-size:8px">Email</h3>
    <p class="copy abs" style="left:58px;top:196px;font-size:3.5px">info@brackwell.com.au</p>
    <div class="field" style="left:188px;top:115px;width:45px;height:10px;font-size:3px">Your Name*</div>
    <div class="field" style="left:239px;top:115px;width:47px;height:10px;font-size:3px">Last Name*</div>
    <div class="field" style="left:188px;top:129px;width:45px;height:10px;font-size:3px">Phone Number*</div>
    <div class="field" style="left:239px;top:129px;width:47px;height:10px;font-size:3px">Email*</div>
    <div class="field" style="left:188px;top:143px;width:98px;height:26px;font-size:3px">Message</div>
    <div class="submit" style="left:188px;top:176px;width:40px;height:8px;font-size:3px;line-height:8px">Submit</div>
    <div class="abs" style="left:42px;top:236px;font-size:3px;color:#555;display:flex;gap:8px;font-weight:400"><span>Home</span><span>Our Service</span><span>Product</span><span>Pricing</span><span>About Us</span><span>Contact Us</span></div>
    <div class="abs" style="left:276px;top:236px;font-size:3px;color:#333">+ 0400 123 456</div>
    <div class="footer-line" style="top:246px"></div>
    <p class="abs" style="left:42px;top:262px;font-size:3px;color:#888">© 2025 All Rights Reserved</p>
    <p class="legal" style="top:271px;height:12px;font-size:3px;padding:4px 42px">Lorem ipsum dolor sit amet, consectetur adipiscing elit. Ut elit tellus, luctus nec ullamcorper mattis, pulvinar dapibus leo.</p>
  </section>
</main>

<!-- ================= MOBILE ================= -->
<main class="screen mobile" aria-label="Mobile homepage">
  <div class="topbar" style="height:8px;font-size:2.5px;gap:6px;padding:0 6px">
    <span>☎ 0400 123 456</span><span>✉ info@brackwell.com.au</span><span>⌖ PO Box 1180, Eastmere Q 4100</span>
  </div>
  <nav class="nav" style="top:8px;height:30px;padding:0 8px;font-size:3px">
    <div class="brand" style="font-size:3px"><span class="brand-mark" style="width:4px;height:4px"></span>Brackwell Renovations</div>
    <div class="nav-links" style="gap:5px"><span>Home</span><span>Our Service</span><span>Product</span><span>Pricing</span><span>About Us</span><span>Contact Us</span></div>
  </nav>

  <header class="hero" role="img" aria-label="Photo of a spacious living room with city view at dusk" style="top:38px;height:200px;clip-path:polygon(0 0,100% 0,100% 82%,65% 100%,0 86%)">
    <h1 style="font-size:11.5px;margin-top:52px">Crafting Your Dream<br>Home,<br>Room by Room</h1>
    <p style="font-size:3.5px;width:185px;margin:3px auto 0">At Brackwell Renovation, we transform houses into homes with expert residential remodeling services. Specializing in kitchens, bathrooms, basements, additions, and custom interiors, we bring craftsmanship and care to every project. Discover how we can elevate your living space today.</p>
  </header>

  <section class="fade" style="top:215px;height:245px">
    <nav class="nav" style="top:35px;height:12px;padding:0 8px;font-size:2.6px">
      <div class="brand" style="font-size:2.6px"><span class="brand-mark" style="width:4px;height:4px"></span>Brackwell Renovations</div>
      <div class="nav-links" style="gap:5px"><span>Home</span><span>Our Service</span><span>Product</span><span>Pricing</span><span>About Us</span><span>Contact Us</span></div>
    </nav>
    <p class="copy abs" style="left:8px;top:50px;width:115px;font-size:3.5px">homes with expert residential remodeling services. Specializing in kitchens, bathrooms, basements, additions, and custom interiors, we bring craftsmanship and care to every project. Discover how we can elevate your living space today.</p>
    <div class="pill solid" style="left:163px;top:63px;width:40px;height:11px;font-size:4px;line-height:11px">CALL US</div>
    <div class="photo light" role="img" aria-label="Living room with sculptural lamp" style="left:8px;top:114px;width:62px;height:100px"></div>
    <div class="photo" role="img" aria-label="Bright room with plants and armchairs" style="left:75px;top:114px;width:62px;height:100px"></div>
    <div class="photo" role="img" aria-label="Lounge with timber ceiling" style="left:142px;top:114px;width:62px;height:100px"></div>
    <div class="wedge" style="top:225px;height:21px;clip-path:polygon(0 100%,0 60%,52% 0,100% 55%,100% 100%)"></div>
  </section>

  <section aria-label="Who we are" style="text-align:center">
    <h2 class="h-teal abs" style="left:0;width:213px;top:479px;font-size:11px">Who We Are?</h2>
    <p class="copy abs" style="left:8px;top:500px;width:197px;font-size:3.4px">With years of experience in general contracting, Brackwell Renovation is your trusted partner for residential remodeling. We pride ourselves on delivering high-quality renovations tailored to your vision, whether it’s a modern kitchen, a spa-like bathroom, or a custom basement retreat. Our commitment to detail, reliability, and client satisfaction sets us apart. Let us bring your ideas to life with precision and style.</p>
    <div class="photo light" role="img" aria-label="White kitchen with island and stools" style="left:8px;top:551px;width:196px;height:131px"></div>
  </section>

  <section class="fade" style="top:682px;height:418px;background:linear-gradient(180deg,#fff 0%,var(--teal-soft) 40%,#9ee6dd 75%,var(--teal) 100%);text-align:center">
    <h3 class="h-teal abs" style="left:0;width:213px;top:17px;font-size:11px">Sleek Kitchen with<br>Clean Accents</h3>
    <p class="copy abs" style="left:40px;top:58px;width:133px;font-size:3px">Step into elegance with a kitchen that’s as functional as it is beautiful. At Brackwell Renovation, we blend expert craftsmanship with custom design to create spaces that inspire daily living. This remodel showcases our dedication to quality and style.</p>
    <div class="pill soft" style="left:45px;top:94px;width:30px;height:11px;font-size:5px;line-height:11px">Call Us</div>
    <div class="photo dark" role="img" aria-label="Living room with stone feature wall" style="left:6px;top:125px;width:206px;height:75px"></div>
    <h3 class="h-teal abs" style="left:46px;top:228px;font-size:11px;text-align:left">Finished Basement<br>with Cozy Seating</h3>
    <p class="copy abs" style="left:46px;top:266px;width:125px;font-size:3px;text-align:left;color:#4b6b67">Unlock the potential of your basement with Brackwell Renovation. This inviting lounge demonstrates our ability to turn unused spaces into warm, functional retreats—perfect for family time or quiet evenings.</p>
    <div class="pill soft" style="left:46px;top:300px;width:30px;height:11px;font-size:5px;line-height:11px;background:#e0f8f4">Call Us</div>
    <div class="photo" role="img" aria-label="Dining area with pendant lights and artwork" style="left:6px;top:332px;width:206px;height:75px"></div>
  </section>

  <section class="about" role="img" aria-label="Dim living room backdrop" style="top:1100px;height:174px">
    <p style="font-size:9.5px;margin-top:24px;font-weight:400">About Us</p>
    <p style="font-size:12px;color:var(--teal)">Brackwell Renovation</p>
    <p style="font-size:3.3px;width:200px;margin:3px auto 0;font-weight:400;line-height:1.4">At Brackwell Renovation, we transform houses into homes with expert residential remodeling services. Specializing in kitchens, bathrooms, basements, additions, and custom interiors, we bring craftsmanship and care to every project. Discover how we can elevate your living space today.</p>
    <div class="pill solid" style="left:79px;top:88px;width:54px;height:12px;font-size:5.5px;line-height:12px;border-radius:1px">Contact Us</div>
    <div class="abs" style="left:18px;top:130px;width:182px;display:flex;justify-content:space-between">
      <div class="stat"><b style="font-size:10px">175</b><span style="font-size:3px">Happy clients</span></div>
      <div class="stat"><b style="font-size:10px">300+</b><span style="font-size:3px">Projects<br>completed</span></div>
      <div class="stat"><b style="font-size:10px">9+</b><span style="font-size:3px">Projects<br>Managed</span></div>
      <div class="stat"><b style="font-size:10px">180+</b><span style="font-size:3px">Dedicated<br>employees</span></div>
    </div>
  </section>

  <section class="services" style="top:1274px;height:295px">
    <h2 class="h-teal" style="font-size:10.5px;margin-top:2px">Our Services</h2>
    <p class="copy" style="font-size:2.8px">We also offer custom interiors and more—contact us to discuss your unique project!</p>
    <article class="card" style="left:8px;top:55px;width:94px">
      <div class="photo site" role="img" aria-label="Builder on a residential site" style="position:relative;width:94px;height:40px"></div>
      <h4 style="font-size:3.8px;margin-top:10px">Kitchens</h4>
      <p style="font-size:3.2px">From custom cabinetry to open-plan designs, we create kitchens that blend functionality with elegance</p>
      <a style="font-size:3.2px">Read More</a>
    </article>
    <article class="card" style="left:110px;top:57px;width:94px">
      <div class="photo site" role="img" aria-label="Contractors reviewing plans" style="position:relative;width:94px;height:40px"></div>
      <h4 style="font-size:3.8px;margin-top:6px">Bathrooms</h4>
      <p style="font-size:3.2px">Turn your bathroom into a luxurious oasis with our expert tiling, fixtures, and layouts</p>
      <a style="font-size:3.2px">Read More</a>
    </article>
    <article class="card" style="left:8px;top:172px;width:94px">
      <div class="photo site" role="img" aria-label="Engineers with tablet on site" style="position:relative;width:94px;height:40px"></div>
      <h4 style="font-size:3.8px;margin-top:9px">Basements &amp; Additions</h4>
      <p style="font-size:3.2px">Expand your living space with beautifully crafted basements and seamless home additions</p>
      <a style="font-size:3.2px">Read More</a>
    </article>
    <article class="card" style="left:110px;top:172px;width:94px">
      <div class="photo site" role="img" aria-label="Team studying drawings on site" style="position:relative;width:94px;height:40px"></div>
      <h4 style="font-size:3.8px;margin-top:9px">Rooms</h4>
      <p style="font-size:3.2px">From custom cabinetry to open-plan designs, we create kitchens that blend functionality with elegance</p>
      <a style="font-size:3.2px">Read More</a>
    </article>
  </section>

  <section class="projects" style="top:1557px;height:540px">
    <svg class="abs" style="left:0;top:0" width="213" height="8" viewBox="0 0 213 8" aria-hidden="true"><path d="M0 0H213V3C180 6 150 1 110 4S40 2 0 5Z" fill="#f3f3f3"/></svg>
    <h2 class="h-teal" style="font-size:10.5px;margin-top:8px">Our Project</h2>
    <p style="font-size:4px;color:#e0762b;font-weight:500;margin-top:8px">Workshop Name</p>
    <div class="grid" role="img" aria-label="Gallery of finished interior projects" style="left:8px;top:50px;width:196px;height:262px;grid-template-columns:repeat(3,1fr);grid-template-rows:repeat(4,1fr)">
      <div class="tile"></div><div class="tile"></div><div class="tile"></div>
      <div class="tile"></div><div class="tile"></div><div class="tile"></div>
      <div class="tile"></div><div class="tile"></div><div class="tile"></div>
      <div class="tile"></div><div class="tile"></div><div class="tile"></div>
    </div>
    <p class="quote" style="font-size:4px;margin-top:318px;padding:0 24px">“What really turned me over was the ability to understand how everything works without any prior knowledge”</p>
    <p style="font-size:3.5px;color:var(--amber);margin-top:4px"><span class="avatar" style="width:14px;height:14px"></span> John Doe</p>
    <p class="trusted" style="font-size:10px;margin-top:40px">Your Trusted Partner in<br>Construction Oversight<br>and Planning</p>
    <p style="font-size:3.5px;color:#ccc">Harbourline Australia Pty Ltd</p>
  </section>

  <section class="contact" style="top:2075px;height:332px;clip-path:polygon(0 22px,48% 0,100% 22px,100% 100%,0 100%)">
    <div class="brand abs" style="left:68px;top:22px;font-size:6px"><span class="brand-mark" style="width:9px;height:9px"></span>Brackwell Renovations</div>
    <h2 class="h-teal abs" style="left:0;width:213px;top:41px;font-size:11px;text-align:center">Contact Us</h2>
    <p class="copy abs" style="left:0;width:213px;top:56px;font-size:3px;text-align:center">We would love to speak with you.<br>Feel free to reach us</p>
    <h3 class="h-teal abs" style="left:10px;top:78px;font-size:9px">Address</h3>
    <p class="copy abs" style="left:10px;top:89px;font-size:3.4px">PO Box 1180, Eastmere Q 4100</p>
    <h3 class="h-teal abs" style="left:10px;top:107px;font-size:9px">Phone</h3>
    <p class="copy abs" style="left:10px;top:119px;font-size:3.4px">0400 123 456</p>
    <h3 class="h-teal abs" style="left:10px;top:137px;font-size:9px">Email</h3>
    <p class="copy abs" style="left:10px;top:149px;font-size:3.4px">info@brackwell.com.au</p>
    <div class="field" style="left:10px;top:168px;width:92px;height:13px;font-size:3px">Your Name*</div>
    <div class="field" style="left:110px;top:168px;width:92px;height:13px;font-size:3px">Last Name*</div>
    <div class="field" style="left:10px;top:187px;width:92px;height:13px;font-size:3px">Phone Number*</div>
    <div class="field" style="left:110px;top:187px;width:92px;height:13px;font-size:3px">Email*</div>
    <div class="field" style="left:10px;top:207px;width:192px;height:33px;font-size:3px">Message</div>
    <div class="submit" style="left:74px;top:249px;width:64px;height:13px;font-size:3.5px;line-height:13px">Submit</div>
    <div class="abs" style="left:4px;top:270px;font-size:2.6px;color:#555;display:flex;gap:7px;font-weight:400"><span>Home</span><span>Our Service</span><span>Product</span><span>Pricing</span><span>About Us</span></div>
    <div class="abs" style="left:4px;top:279px;font-size:2.6px;color:#555">Contact Us</div>
    <div class="abs" style="left:169px;top:274px;font-size:4px;color:#333">+ 0400 123 456</div>
    <div class="footer-line" style="top:290px"></div>
    <p class="abs" style="left:4px;top:307px;font-size:2.8px;color:#888">© 2025 All Rights Reserved</p>
    <p class="legal" style="top:318px;height:14px;font-size:2.8px;padding:2px 4px">Lorem ipsum dolor sit amet, consectetur adipiscing elit. Ut elit tellus, luctus nec ullamcorper mattis, pulvinar dapibus leo.</p>
  </section>
</main>

</body>
</html>
```